Junk Removal Website Design

We are working with a Junk Removal company in California. They provide junk hauling services for commercial and residential throughout California.
Some sites to use for inspiration:
https://www.clearbarrowhauls.com
https://pebblecartworkteam.com
https://www.fernwayliftersandmovers.com
https://www.mistoakcleanupcrew.com
Thank you for taking the time to consider designing a website for us. We are web developers based in Stockton, CA, USA. Most of our projects go through the same process. Understanding this process may help you win a project with us. We custom-code all of our websites in-house. We don’t have any requirements as to what tools you use for your design, but we ask that you follow these guidelines.
IMAGES:
If you use any images or icons in the design, we ask that you have a link to the asset so we can purchase the image/icon. Most of the designs we submit do not have the customer’s images on them unless they have some great images. Be creative; show us the feeling you are trying to portray with your image choices. Use any royalty-free site you choose. We subscribe to Vontrel and mainly use their images, but we can purchase images outside of Vontrel. PLEASE NOTE: we will not submit designs to clients with watermarks on the images.
FONTS:
We ask that you identify the fonts you’re using in the design. This can be done in a message if you want. We typically use Quimbly Fonts and Vontrel Fonts.
CONTENT:
We're always open to different content and ideas. We often submit designs with stock images so the client can see our vision. We typically take pictures after the website launch to use their images with our vision. Lorem Ipsum is fine for paragraphs, but we ask that you make the Headers with correct English. We want to be able to show the vision and identify the sections of the website.
INSPIRATION:
We typically add a couple of links in the brief of websites we like to help you get started in your design.
REVISIONS:
We do not often ask for revisions of the designs unless we see something in the design that may not appeal to the client. If there are slight changes that we want to make, we do that in the development process.
FEEDBACK:
We rarely give feedback on designs during the design process. We are working on many website projects and do not have the time to provide feedback. We usually respond if your request is well thought out and asks specific questions, but a note asking “feedback, please” usually goes unanswered.
Number of Pages Required
1 page

```html
<!DOCTYPE html>
<html lang="en">
<head>
<meta charset="utf-8">
<title>Junk Removal – Stress-Free Moving &amp; Junk Removal</title>
<link href="https://fonts.googleapis.com/css2?family=Barlow+Condensed:wght@500;600;700&family=Exo+2:ital,wght@1,800;1,900&family=Open+Sans:wght@400;600;700&display=swap" rel="stylesheet">
<style>
:root{
  --green:#3f9f34;
  --green-dark:#2f8a27;
  --ink:#231f20;
  --white:#ffffff;
  --grey-text:#3b3b3b;
  --card-shadow:rgba(0,0,0,.12);
}
*{box-sizing:border-box;margin:0;padding:0}
html,body{width:1200px;height:3376px;overflow:hidden;background:var(--white)}
body{position:relative;font-family:"Open Sans",Arial,sans-serif;color:var(--ink)}
.abs{position:absolute}
.cond{font-family:"Barlow Condensed","Arial Narrow",sans-serif;text-transform:uppercase}
.display{font-family:"Exo 2","Arial Black",sans-serif;font-style:italic;font-weight:900;text-transform:uppercase}
.btn{position:absolute;display:flex;align-items:center;justify-content:center;font-family:"Open Sans",Arial,sans-serif;font-weight:700;font-size:15px;color:var(--white);border-radius:3px;text-transform:uppercase}
.btn--green{background:var(--green)}
.btn--dark{background:var(--ink)}
.lorem{font-size:11px;line-height:20px}

/* header */
.brand{left:161px;top:14px;width:160px;font-family:"Barlow Condensed",sans-serif;font-weight:700;font-size:40px;line-height:36px;color:var(--ink);text-transform:uppercase;letter-spacing:1px}
.phone{left:737px;top:20px;display:flex;align-items:center;gap:10px;font-size:20px;font-weight:600}
.phone__icon{width:32px;height:30px;background:var(--green);border-radius:3px;display:flex;align-items:center;justify-content:center}
.nav{left:384px;top:72px;width:652px;display:flex;justify-content:space-between;font-size:13px;font-weight:600;text-transform:uppercase}

/* hero */
.hero{left:0;top:104px;width:1200px;height:624px;background:linear-gradient(100deg,#6a7f3a 0%,#7fa944 30%,#9a8a5a 55%,#4f6a33 80%,#3c5528 100%)}
.hero__title{right:164px;top:178px;text-align:right;font-size:58px;line-height:63px;color:var(--white);text-transform:none}

/* features */
.features{left:161px;top:620px;width:875px;height:260px;display:flex;border-radius:40px 40px 0 0;overflow:hidden}
.feature{height:100%;display:flex;flex-direction:column;align-items:center;color:var(--white);text-align:center;padding-top:52px}
.feature h3{font-size:25px;font-weight:600;margin-top:16px;margin-bottom:10px}
.feature p{font-size:11px;line-height:16px;width:240px}
.feature--green{background:var(--green)}
.feature--dark{background:var(--ink)}
.corner-dot{width:68px;height:68px;border-radius:50%;background:var(--green);border:6px solid var(--white)}

/* section headings */
.heading{font-size:46px;color:var(--green);text-align:center;width:1200px;left:0}

/* services */
.service{width:290px}
.service h4{font-size:21px;font-weight:600;margin-bottom:8px;white-space:nowrap}
.service p{font-size:11px;line-height:16px;color:var(--grey-text);width:232px}
.service--left{text-align:right}
.service--left p{margin-left:auto}
.svc-icon{width:80px;height:80px;border-radius:50%;border:5px solid var(--white);display:flex;align-items:center;justify-content:center}

/* dark section */
.junk{left:0;top:1407px;width:1200px;height:500px;background:var(--ink)}
.junk__body{color:var(--white)}
.junk__body p{margin-bottom:13px}

/* split */
.commercial{left:0;top:1906px;width:600px;height:428px;background:var(--green)}
.split-title{font-size:44px}

/* clients */
.clients-bg{left:0;top:2334px;width:1200px;height:654px;background:linear-gradient(180deg,#f6f8f4 0%,#eef1ea 60%,#f1f3ee 100%)}
.card{width:277px;height:181px;border-radius:16px;background:var(--white);box-shadow:0 3px 10px var(--card-shadow);padding:36px 12px 0}
.card--dark{background:var(--ink);color:var(--white)}
.card h5{font-size:23px;font-weight:600;margin-bottom:8px}
.card p{font-size:11px;line-height:16px;width:235px}
.card .author{font-family:"Barlow Condensed",sans-serif;font-weight:600;font-size:15px;margin-top:14px;text-transform:uppercase}
.card .quote{position:absolute;right:6px;top:-14px;font-family:Georgia,serif;font-weight:700;font-size:120px;line-height:120px;color:var(--green)}

/* footer */
.footer{left:0;top:2987px;width:1200px;height:389px;background:var(--ink);color:var(--white)}
.footer-title{font-size:24px;font-weight:600;color:var(--white)}
.links{list-style:none;font-size:11.5px;font-weight:600;line-height:20px;text-transform:uppercase}
.field{background:var(--white);border:1px solid #ccc;color:var(--ink);font-size:12px;font-weight:600;padding:10px 6px}
</style>
</head>
<body>

<!-- header -->
<div class="abs brand">Junk<br>Removal</div>
<div class="abs phone">
  <span class="phone__icon"><svg width="18" height="18" viewBox="0 0 24 24"><path fill="#fff" d="M6.6 10.8a15.1 15.1 0 0 0 6.6 6.6l2.2-2.2c.3-.3.7-.4 1-.2 1.1.4 2.3.6 3.6.6.6 0 1 .4 1 1V20c0 .6-.4 1-1 1A17 17 0 0 1 3 4c0-.6.4-1 1-1h3.5c.6 0 1 .4 1 1 0 1.3.2 2.5.6 3.6.1.3 0 .7-.2 1z"/></svg></span>
  1-800-555-0142
</div>
<div class="btn btn--green" style="left:947px;top:20px;width:89px;height:31px;font-size:12.5px">Book Now</div>
<nav class="abs nav"><span>Home</span><span>Who We Are</span><span>What We Remove</span><span>Jobs We Do</span><span>Our Work</span><span>Blog</span><span>FAQ</span><span>Contact Us</span></nav>

<!-- hero -->
<div class="abs hero" role="img" aria-label="Photo of a worker in a hard hat and safety vest beside a green garbage truck and a yellow bin"></div>
<h1 class="abs display hero__title">Stress-Free<br>Moving &amp; Junk<br>Removal</h1>
<div class="btn btn--green" style="left:922px;top:385px;width:114px;height:38px">Get a Quote</div>

<!-- features -->
<div class="abs corner-dot" style="left:127px;top:838px"></div>
<div class="abs corner-dot" style="left:1002px;top:838px"></div>
<div class="abs features">
  <div class="feature feature--green" style="width:287px">
    <svg width="60" height="58" viewBox="0 0 60 58"><path d="M30 4a14 14 0 0 0-14 14c0 11 14 26 14 26s14-15 14-26A14 14 0 0 0 30 4z" fill="none" stroke="#fff" stroke-width="4"/><circle cx="30" cy="18" r="5" fill="#fff"/><ellipse cx="30" cy="48" rx="26" ry="7" fill="none" stroke="#fff" stroke-width="4"/></svg>
    <h3 class="cond">Find a Location</h3>
    <p>Nemo enim ipsam voluptatem quia volup tas sit aspernatur aut odit aut fugit sed quia consequuntur magni dolores</p>
  </div>
  <div class="feature feature--dark" style="width:304px">
    <svg width="60" height="58" viewBox="0 0 60 58"><circle cx="30" cy="20" r="16" fill="none" stroke="#fff" stroke-width="3"/><text x="30" y="28" text-anchor="middle" font-family="Open Sans,sans-serif" font-weight="700" font-size="22" fill="#fff">$</text><path d="M6 46c8-6 16-6 24-2h12c3 0 3 4 0 4H30m-24 6l8-4 14 4 22-8" fill="none" stroke="#fff" stroke-width="3" stroke-linecap="round"/></svg>
    <h3 class="cond">Our Pricing</h3>
    <p>Nemo enim ipsam voluptatem quia volup tas sit aspernatur aut odit aut fugit sed quia consequuntur magni dolores</p>
  </div>
  <div class="feature feature--green" style="width:284px">
    <div style="height:58px;font-family:Georgia,serif;font-weight:700;font-size:110px;line-height:100px">&ldquo;</div>
    <h3 class="cond">Get a Free Quote Online</h3>
    <p>Nemo enim ipsam voluptatem quia volup tas sit aspernatur aut odit aut fugit sed quia consequuntur magni dolores</p>
  </div>
</div>

<!-- services -->
<h2 class="abs display heading" style="top:958px">Our Services</h2>
<div class="abs" style="left:483px;top:1050px;width:234px;height:285px;background:var(--green);border-radius:0 0 40px 40px"></div>
<div class="abs" style="left:483px;top:1063px;width:234px;height:234px;border-radius:50%;background:var(--ink);display:flex;align-items:center;justify-content:center;color:#fff;font-family:'Barlow Condensed',sans-serif;font-weight:700;font-size:38px;line-height:34px;text-align:center;text-transform:uppercase">Junk<br>Removal</div>

<div class="abs svc-icon" style="left:444px;top:1082px;background:var(--green)"><svg width="42" height="34" viewBox="0 0 42 34"><rect x="2" y="6" width="22" height="16" fill="#fff"/><path d="M24 10h9l6 7v5H24z" fill="#fff"/><circle cx="10" cy="26" r="4" fill="#fff"/><circle cx="32" cy="26" r="4" fill="#fff"/></svg></div>
<div class="abs svc-icon" style="left:444px;top:1200px;background:var(--ink)"><svg width="38" height="38" viewBox="0 0 38 38"><path d="M19 3l15 7v18l-15 7-15-7V10z" fill="none" stroke="#fff" stroke-width="3"/><path d="M4 10l15 7 15-7M19 17v18" fill="none" stroke="#fff" stroke-width="3"/></svg></div>
<div class="abs svc-icon" style="left:676px;top:1082px;background:var(--ink)"><svg width="32" height="38" viewBox="0 0 32 38"><path d="M4 8h24M12 8V4h8v4M7 8l2 27h14l2-27" fill="none" stroke="#fff" stroke-width="3"/><path d="M13 14v16M19 14v16" stroke="#fff" stroke-width="2"/></svg></div>
<div class="abs svc-icon" style="left:676px;top:1200px;background:var(--green)"><svg width="38" height="38" viewBox="0 0 38 38"><rect x="6" y="24" width="26" height="10" fill="none" stroke="#fff" stroke-width="3"/><path d="M14 24l12-18 5 4-10 14" fill="none" stroke="#fff" stroke-width="3"/></svg></div>

<div class="abs service service--left" style="left:148px;top:1092px"><h4 class="cond">Full-Service Moving Company</h4><p>Nemo enim ipsam voluptatem quia volup tas sit aspernatur aut odit aut fugit sed quia consequuntur magni dolores</p></div>
<div class="abs service service--left" style="left:148px;top:1205px"><h4 class="cond">Hourly Moving &amp; Packing Services</h4><p>Nemo enim ipsam voluptatem quia volup tas sit aspernatur aut odit aut fugit sed quia consequuntur magni dolores</p></div>
<div class="abs service" style="left:762px;top:1092px"><h4 class="cond">Junk Removal &amp; Trash Pickup</h4><p>Nemo enim ipsam voluptatem quia volup tas sit aspernatur aut odit aut fugit sed quia consequuntur magni dolores</p></div>
<div class="abs service" style="left:762px;top:1205px"><h4 class="cond">Donation Pickups</h4><p>Nemo enim ipsam voluptatem quia volup tas sit aspernatur aut odit aut fugit sed quia consequuntur magni dolores</p></div>

<!-- junk removal -->
<section class="abs junk"></section>
<h2 class="abs display" style="left:161px;top:1484px;font-size:46px;color:#fff">Junk Removal</h2>
<div class="abs junk__body lorem" style="left:161px;top:1553px;width:432px">
  <p>Nemo enim ipsam voluptatem quia voluptas sit aspernatur aut odit aut fugit, sed quia consequuntur magni dolores eos qui ratione voluptatem sequi nesciunt. Neque porro quisquam est, qui dolorem ipsum quia dolor sit amet, consectetur, adipisci velit, sed quia non numquam eius modi tempora incidunt ut labore et dolore magnam aliquam quaerat voluptatem.</p>
  <p>Nemo enim ipsam voluptatem quia voluptas sit aspernatur aut odit aut fugit, sed quia consequuntur magni dolores eos qui ratione voluptatem sequi nesciunt. Neque porro quisquam est, qui dolorem ipsum quia dolor sit amet, consectetur, adipisci velit, sed quia non numquam eius modi tempora incidunt ut labore et dolore magnam aliquam quaerat voluptatem.</p>
</div>
<div class="btn btn--green" style="left:161px;top:1800px;width:117px;height:36px">Read More</div>
<div class="abs" style="left:640px;top:1465px;width:396px;height:390px;background:linear-gradient(160deg,#cfcfcf 0%,#bdbdbd 45%,#3fb964 70%,#2e9a4f 100%);border-radius:8px" role="img" aria-label="Illustration of a grey box truck with a green cab"></div>

<!-- commercial / residential -->
<section class="abs commercial" role="img" aria-label="Faint photo of a commercial building under construction on a green overlay"></section>
<svg class="abs" style="left:161px;top:1958px" width="74" height="72" viewBox="0 0 74 72"><path d="M2 70V24l24-8v54zM30 70V6l42-6v70z" fill="#fff"/><g fill="#3f9f34"><rect x="36" y="12" width="8" height="8"/><rect x="50" y="12" width="8" height="8"/><rect x="36" y="28" width="8" height="8"/><rect x="50" y="28" width="8" height="8"/><rect x="36" y="44" width="8" height="8"/><rect x="50" y="44" width="8" height="8"/><rect x="8" y="34" width="12" height="5"/><rect x="8" y="46" width="12" height="5"/></g></svg>
<h2 class="abs display split-title" style="left:161px;top:2040px;color:#fff">Commercial</h2>
<p class="abs lorem" style="left:161px;top:2104px;width:410px;color:#fff;text-align:justify">Nemo enim ipsam voluptatem quia voluptas sit aspernatur aut odit aut fugit, sed quia consequuntur magni dolores eos qui ratione voluptatem sequi nesciunt. Neque porro quisquam est, qui dolorem ipsum quia dolor sit amet, consectetur, adipisci velit, sed quia non numquam eius modi tempora incidunt ut labore et dolore magnam aliquam quaerat voluptatem.</p>
<div class="btn btn--dark" style="left:161px;top:2232px;width:117px;height:36px">Read More</div>

<svg class="abs" style="left:630px;top:1958px" width="72" height="70" viewBox="0 0 72 70"><path d="M36 2L2 24h8v44h52V24h8z" fill="#231f20"/><g fill="#fff"><rect x="18" y="30" width="8" height="8"/><rect x="32" y="30" width="8" height="8"/><rect x="46" y="30" width="8" height="8"/><rect x="18" y="46" width="8" height="8"/><rect x="46" y="46" width="8" height="8"/><rect x="32" y="48" width="8" height="20"/></g></svg>
<h2 class="abs display split-title" style="left:629px;top:2040px;color:var(--ink)">Residential</h2>
<p class="abs lorem" style="left:629px;top:2104px;width:408px;color:var(--grey-text);text-align:justify">Nemo enim ipsam voluptatem quia voluptas sit aspernatur aut odit aut fugit, sed quia consequuntur magni dolores eos qui ratione voluptatem sequi nesciunt. Neque porro quisquam est, qui dolorem ipsum quia dolor sit amet, consectetur, adipisci velit, sed quia non numquam eius modi tempora incidunt ut labore et dolore magnam aliquam quaerat voluptatem.</p>
<div class="btn btn--dark" style="left:629px;top:2232px;width:117px;height:36px">Read More</div>

<!-- clients -->
<section class="abs clients-bg" role="img" aria-label="Faded background photo of a garbage truck on a street"></section>
<h2 class="abs display heading" style="top:2402px">Our Happy Clients</h2>

<div class="abs card" style="left:161px;top:2504px"><span class="quote">&rdquo;</span><h5 class="cond">Had a Great Service</h5><p>Nemo enim ipsam voluptatem quia volup tas sit aspernatur aut odit aut fugit sed quia consequuntur magni dolores</p><div class="author">- John Smith</div></div>
<div class="abs card card--dark" style="left:461px;top:2504px"><span class="quote" style="color:#fff">&rdquo;</span><h5 class="cond">Had a Great Service</h5><p>Nemo enim ipsam voluptatem quia volup tas sit aspernatur aut odit aut fugit sed quia consequuntur magni dolores</p><div class="author">- Andrews</div></div>
<div class="abs card" style="left:760px;top:2504px"><span class="quote">&rdquo;</span><h5 class="cond">Had a Great Service</h5><p>Nemo enim ipsam voluptatem quia volup tas sit aspernatur aut odit aut fugit sed quia consequuntur magni dolores</p><div class="author">- Clara James</div></div>
<div class="abs card" style="left:161px;top:2717px"><span class="quote">&rdquo;</span><h5 class="cond">Had a Great Service</h5><p>Nemo enim ipsam voluptatem quia volup tas sit aspernatur aut odit aut fugit sed quia consequuntur magni dolores</p><div class="author">- Jack Bardom</div></div>
<div class="abs card" style="left:461px;top:2717px"><span class="quote">&rdquo;</span><h5 class="cond">Had a Great Service</h5><p>Nemo enim ipsam voluptatem quia volup tas sit aspernatur aut odit aut fugit sed quia consequuntur magni dolores</p><div class="author">- Emily John</div></div>
<div class="abs card" style="left:760px;top:2717px"><span class="quote">&rdquo;</span><h5 class="cond">Had a Great Service</h5><p>Nemo enim ipsam voluptatem quia volup tas sit aspernatur aut odit aut fugit sed quia consequuntur magni dolores</p><div class="author">- John Smith</div></div>

<!-- footer -->
<footer class="abs footer"></footer>
<div class="abs" style="left:161px;top:3110px;font-family:'Barlow Condensed',sans-serif;font-weight:700;font-size:62px;line-height:56px;color:#fff;text-transform:uppercase">Junk<br>Removal</div>
<h6 class="abs cond footer-title" style="left:475px;top:3058px">Quick Links</h6>
<ul class="abs links" style="left:475px;top:3098px;color:#fff">
  <li>Home</li><li>Who We Are</li><li>What We Remove</li><li>Jobs We Do</li><li>Our Work</li><li>Blog</li><li>FAQ</li><li>Contact Us</li>
</ul>
<h6 class="abs cond footer-title" style="left:671px;top:3058px">Get in Touch</h6>
<div class="abs field" style="left:671px;top:3099px;width:178px;height:38px">Email</div>
<div class="abs field" style="left:858px;top:3099px;width:178px;height:38px">Number</div>
<div class="abs field" style="left:671px;top:3150px;width:365px;height:70px">Message</div>
<div class="btn btn--green" style="left:671px;top:3235px;width:100px;height:36px;font-size:13.5px">Subscribe</div>
<div class="abs" style="left:161px;top:3308px;width:875px;height:1px;background:#6a6a6a"></div>
<p class="abs" style="left:0;top:3332px;width:1200px;text-align:center;font-size:14px;color:#fff">Copyrights @ 2023 Junk Removal. All Rights Reserved.</p>

</body>
</html>
```